Fernhollow Glow Clinic is a rebranding of fernhollowfootcare.com.au. The business provides Medical Injectables (botox and fillers) Laser and IPL therapies, Podiatry and remedial massage. We have a logo already done (yay! sketch hive!) you can download it here: http://fernhollowglowclinic.com/brand_assets.zip . We are after a clean, long scrolling website (in the style of quvaret.com). There will be 6 subpages (or sections depending on how you create it) (1) Cosmetic Injections (2) Podiatry (3) Remedial Massage (4) Laser Therapies (5) Skin Care (6) Customer Club and Special Offers. The target demographic is wealthy or aspirational women 35+.

Font styles to use
Sans Serif

Colors
9bcb3c
33a6d7

Requirements
Must have
• Simple, clean long scroller like quvaret.com
Nice to have
• Congruence with existing corporate identity.

```html
<!DOCTYPE html>
<html lang="en">
<head>
<meta charset="utf-8">
<title>Fernhollow Glow Clinic</title>
<link href="https://fonts.googleapis.com/css2?family=Raleway:wght@300;400;500;600;700&display=swap" rel="stylesheet">
<style>
:root{
  --green:#9bcb3c;
  --green-dark:#8bbb2e;
  --blue:#33a6d7;
  --blue-band:#1ba1db;
  --hero-bg:#e7f3fd;
  --grey-bg:#eeeeee;
  --ink:#333333;
  --muted:#666666;
  --line:#e2e2e2;
  --price:#a6e2fb;
}
*{box-sizing:border-box;margin:0;padding:0}
html,body{width:1200px;height:2590px;overflow:hidden}
body{font-family:"Raleway",sans-serif;color:var(--ink);background:#fff;font-size:11px;line-height:1.55}
.wrap{width:588px;margin:0 auto;position:relative;height:100%}
section{position:relative}
.btn{display:inline-block;background:var(--green);color:#fff;font-weight:700;font-size:11px;padding:0 22px;height:37px;line-height:37px;border-radius:2px;text-decoration:none}
h2{font-weight:400;font-size:24px;letter-spacing:3px;text-transform:uppercase;color:#222;position:absolute;left:0}
.photo{position:absolute;border-radius:50%;border:6px solid #fff;box-shadow:0 0 0 1px #ddd}

/* header */
.site-header{height:104px;border-bottom:1px solid var(--line)}
.brand{position:absolute;left:0;top:22px;display:flex;align-items:center;gap:8px}
.brand-dot{width:14px;height:14px;border-radius:50%;background:var(--green)}
.brand-name{font-size:18px;font-weight:400;color:#777;letter-spacing:.5px}
.contact{position:absolute;right:0;top:12px;display:flex;gap:14px;font-size:11px}
.contact span{display:flex;align-items:center;gap:5px}
.ico{width:14px;height:14px;border-radius:50%;background:var(--green);display:inline-block}
.social{position:absolute;right:0;top:42px;display:flex;gap:5px}
.social i{width:16px;height:16px;background:#c8c8c8;display:block}
.main-nav{position:absolute;left:0;right:0;top:75px;border-top:1px solid var(--line);height:29px;display:flex;justify-content:space-between;align-items:center;font-size:10.5px;color:#555}
.main-nav .active{color:var(--blue)}

/* hero */
.hero{height:342px;background:var(--hero-bg)}
.hero-photo{position:absolute;left:-64px;top:34px;width:458px;height:308px;background:linear-gradient(120deg,#f3dcc8,#e8c9a8 50%,#f6ead6)}
.hero-copy{position:absolute;left:297px;top:72px;width:300px;font-size:17px;line-height:1.3;color:var(--blue);font-weight:400}
.hero-copy b{font-weight:700}
.hero .btn{position:absolute;left:297px;top:196px}

/* injections */
.injections{height:380px}
.injections h2{top:48px}
.lead{position:absolute;left:0;top:92px;width:300px;font-size:19px;line-height:1.2;color:var(--blue);text-transform:uppercase;font-weight:400}
.offer-title{position:absolute;left:0;top:177px;color:var(--green-dark);font-weight:700;font-size:11px;letter-spacing:1.5px}
.ticks{list-style:none;position:absolute;left:0;top:196px;font-size:10px}
.ticks li{display:flex;align-items:center;gap:7px;height:22px}
.ticks svg{flex:none}
.injections .btn{position:absolute;left:2px;top:286px}

/* podiatry */
.podiatry{height:350px;background:linear-gradient(180deg,#2bb0e5,var(--blue-band));color:#fff}
.podiatry h2{top:48px;color:#fff}
.podiatry .copy{position:absolute;left:217px;top:90px;width:372px;font-size:9.6px;line-height:1.6}
.podiatry .copy p{margin-bottom:12px}
.podiatry .btn{position:absolute;left:217px;top:255px}

/* massage */
.massage{height:351px;background:var(--grey-bg)}
.massage h2{top:48px}
.massage .copy{position:absolute;left:10px;top:86px;width:578px;text-align:center;font-size:9.6px;color:#555}
.price-title{position:absolute;left:0;right:0;top:145px;text-align:center;color:var(--green-dark);font-size:17px;font-weight:600}
.prices{position:absolute;left:0;right:0;top:191px;display:flex;justify-content:center;gap:29px}
.price{width:95px;height:95px;border-radius:50%;background:var(--price);border:5px solid #fff;box-shadow:0 1px 4px rgba(0,0,0,.25);text-align:center;color:#2a7fb0;padding-top:22px}
.price small{display:block;font-size:12px;color:#3d8fbf}
.price strong{font-size:24px;line-height:1;color:#1c8bd0}

/* laser */
.laser{height:318px;background:radial-gradient(ellipse at 60% 0%,#e6f2b6 0%,#b8d968 40%,#93bf3e 100%)}
.laser h2{top:48px}
.laser .copy{position:absolute;left:2px;top:92px;width:586px;font-size:9.6px;color:#333}
.laser .copy p{margin-bottom:12px}
.laser .btn{position:absolute;left:2px;top:233px;background:#86b82f}

/* skin */
.skin{height:345px}
.skin h2{top:46px}
.skin .lead-sm{position:absolute;left:0;top:96px;width:305px;font-size:10.5px;color:var(--blue);line-height:1.4}
.skin .ticks{top:166px}
.skin .ticks b{color:var(--blue)}

/* club */
.club{height:331px;background:var(--blue-band);color:#fff}
.club h2{top:46px;color:#fff}
.club .copy{position:absolute;left:2px;top:92px;width:586px;font-size:9.6px}
.club .copy p{margin-bottom:12px}
.club h3{position:absolute;left:2px;top:188px;color:#f2d43a;font-size:18px;font-weight:600}
.club .ticks{top:218px;font-weight:700}

/* footer */
.site-footer{height:69px}
.foot-nav{position:absolute;left:0;right:0;top:13px;text-align:center;font-size:9.5px;color:#555}
.foot-nav span{padding:0 4px;border-right:1px solid #ccc}
.foot-nav span:last-child{border:0}
.foot-row{position:absolute;left:28px;right:8px;top:38px;display:flex;align-items:center;font-size:9.5px}
.copyright{color:var(--green-dark);margin-right:auto}
.foot-row .contact{position:static;margin-right:10px}
.foot-row .social{position:static}
</style>
</head>
<body>

<header class="site-header">
  <div class="wrap">
    <div class="brand"><span class="brand-dot"></span><span class="brand-name">Fernhollow Glow Clinic</span></div>
    <div class="contact">
      <span><i class="ico"></i>(03) 9412 0738</span>
      <span><i class="ico"></i>info@fernhollowfootcare.com.au</span>
    </div>
    <div class="social"><i></i><i></i><i></i><i></i></div>
    <nav class="main-nav">
      <span class="active">Home</span><span>Cosmetic Injections</span><span>Podiatry</span><span>Remedial Massage</span><span>Laser Therapies</span><span>Skin Care</span><span>Customer Club &amp; Special Offers</span>
    </nav>
  </div>
</header>

<section class="hero">
  <div class="wrap">
    <div class="hero-photo" role="img" aria-label="Two smiling women with blonde hair posing together"></div>
    <p class="hero-copy">We work with a variety of <b>light-based technologies</b>, either as primary or secondary therapies, to help us achieve <b>optimal results</b> for our valued clientele.</p>
    <a class="btn">Know More About us</a>
  </div>
</section>

<section class="injections">
  <div class="wrap">
    <h2>Cosmetic Injections</h2>
    <p class="lead">Now offering Relaxa anti-aging injections with Dr. Aleksei Varnov.</p>
    <p class="offer-title">INTRODUCTORY OFFER, INCLUDES:</p>
    <ul class="ticks">
      <li><svg width="11" height="11"><circle cx="5.5" cy="5.5" r="5.5" fill="#33a6d7"/><path d="M3 5.6l1.8 1.8L8 4" stroke="#fff" stroke-width="1.4" fill="none"/></svg>Comprehensive medical skin care consultation &amp; advice</li>
      <li><svg width="11" height="11"><circle cx="5.5" cy="5.5" r="5.5" fill="#33a6d7"/><path d="M3 5.6l1.8 1.8L8 4" stroke="#fff" stroke-width="1.4" fill="none"/></svg>Initial Relaxa anti-aging injection</li>
      <li><svg width="11" height="11"><circle cx="5.5" cy="5.5" r="5.5" fill="#33a6d7"/><path d="M3 5.6l1.8 1.8L8 4" stroke="#fff" stroke-width="1.4" fill="none"/></svg>Follow up consultation at two weeks</li>
      <li><svg width="11" height="11"><circle cx="5.5" cy="5.5" r="5.5" fill="#33a6d7"/><path d="M3 5.6l1.8 1.8L8 4" stroke="#fff" stroke-width="1.4" fill="none"/></svg>Luminae serum starter pack, tailored to your individual skin type</li>
    </ul>
    <a class="btn">Know More</a>
    <div class="photo" role="img" aria-label="Pink orchid flower close-up" style="left:368px;top:71px;width:200px;height:200px;background:radial-gradient(circle at 45% 50%,#e0358f,#c93c93 40%,#f4e8f0 75%)"></div>
  </div>
</section>

<section class="podiatry">
  <div class="wrap">
    <h2>Podiatry</h2>
    <div class="photo" role="img" aria-label="Hands massaging a bare foot" style="left:2px;top:88px;width:200px;height:200px;background:radial-gradient(circle at 50% 50%,#f0c9a8,#d9a380 55%,#9fcbe6 80%)"></div>
    <div class="copy">
      <p>Podiatrists are university trained health professionals who deal with the diagnosis and management of disorders involving the feet and lower limbs. Our podiatrists can help you with a wide range of conditions, as well as liaise with your GP and other health professionals, to get you back on your feet in no time!</p>
      <p>At your first appointment with us, we will run through your medical history with you, taking note of any pre-existing conditions, recent surgeries and medications you may be currently taking. A physical examination may also be done to give us a broader clinical picture of your current issue. We will then put together a treatment plan with you, including frequency of visits required and expected/likely outcomes.</p>
    </div>
    <a class="btn">Know More</a>
  </div>
</section>

<section class="massage">
  <div class="wrap">
    <h2>Remedial Massage</h2>
    <p class="copy">A highly targeted massage involving more focus on residual troublespots and which will generally involve clinical assessment and a results based treatment plan. May include trigger point therapy, myofascial release, stretching and reassessment on a ongoing basis.</p>
    <p class="price-title">Clinic Prices</p>
    <div class="prices">
      <div class="price"><small>30 min</small><strong>$65</strong></div>
      <div class="price"><small>60 min</small><strong>$110</strong></div>
      <div class="price"><small>90 min</small><strong>$150</strong></div>
    </div>
  </div>
</section>

<section class="laser">
  <div class="wrap">
    <h2>Lesar Tharapies</h2>
    <div class="copy">
      <p>Lorem ipsum dolor sit amet, consectetur adipiscing elit. Sed quis nisi euismod, fermentum tellus a, lobortis quam. Vestibulum condimentum mi vitae diam tristique, egestas dignissim diam mattis. Curabitur vel diam in massa porttitor dictum id in lorem. Vivamus faucibus ac leo ac dignissim.</p>
      <p>Maecenas orci est, euismod facilisis feugiat sit amet, semper ut tortor. Donec eleifend accumsan nisl, nec laoreet leo iaculis sit amet. Vivamus varius arcu eu sagittis aliquam. Vivamus accumsan cursus hendrerit. Vivamus eu magna rhoncus, consectetur metus ac, varius lacus. Donec ultricies, tortor quis sagittis sagittis, mauris erat ullamcorper augue, eu placerat diam nunc a lorem. Nam vulputate mauris id arcu pharetra, sed posuere quam cursus.</p>
    </div>
    <a class="btn">Know More</a>
  </div>
</section>

<section class="skin">
  <div class="wrap">
    <h2>Skin Care</h2>
    <p class="lead-sm">We recognise that every skin is different and requires an individualised approach. At your free initial consultation, we will perform a comprehensive skin assessment and formulate an appropriate treatment plan for you.</p>
    <ul class="ticks">
      <li><svg width="11" height="11"><circle cx="5.5" cy="5.5" r="5.5" fill="#9bcb3c"/><path d="M3 5.6l1.8 1.8L8 4" stroke="#fff" stroke-width="1.4" fill="none"/></svg>VelvaDerm Facial <b>(45 min) $155</b></li>
      <li><svg width="11" height="11"><circle cx="5.5" cy="5.5" r="5.5" fill="#9bcb3c"/><path d="M3 5.6l1.8 1.8L8 4" stroke="#fff" stroke-width="1.4" fill="none"/></svg>VelvaDerm Facial &amp; Head/Shoulder Massage <b>(1 hr) $185</b></li>
      <li><svg width="11" height="11"><circle cx="5.5" cy="5.5" r="5.5" fill="#9bcb3c"/><path d="M3 5.6l1.8 1.8L8 4" stroke="#fff" stroke-width="1.4" fill="none"/></svg>Deluxe VelvaDerm Facial &amp; Full Body Massage <b>(1.5hr) $225</b></li>
      <li><svg width="11" height="11"><circle cx="5.5" cy="5.5" r="5.5" fill="#9bcb3c"/><path d="M3 5.6l1.8 1.8L8 4" stroke="#fff" stroke-width="1.4" fill="none"/></svg>Laser Tattoo Removal – approximately <b>$175 for credit card-sized area</b></li>
      <li><svg width="11" height="11"><circle cx="5.5" cy="5.5" r="5.5" fill="#9bcb3c"/><path d="M3 5.6l1.8 1.8L8 4" stroke="#fff" stroke-width="1.4" fill="none"/></svg>LED Light Therapy – <b>$85 (allow ½ hour)</b></li>
    </ul>
    <div class="photo" role="img" aria-label="Hands with a manicure resting on a towel" style="left:368px;top:84px;width:200px;height:200px;background:radial-gradient(circle at 50% 50%,#e9b48e,#d39570 50%,#7fb4d6 85%)"></div>
  </div>
</section>

<section class="club">
  <div class="wrap">
    <h2>Customer Club &amp; Special Offers</h2>
    <div class="copy">
      <p>Cras accumsan orci mauris, ut aliquam ipsum faucibus sed. Fusce quam dui, accumsan a magna in, faucibus tristique lectus. Vestibulum sapien leo, placerat quis luctus eget, auctor et justo. Vestibulum ante ipsum primis in faucibus orci luctus et ultrices posuere cubilia Curae.</p>
      <p>Duis sagittis, risus ut viverra dignissim, lectus nunc iaculis arcu, et gravida est tortor ut erat. Morbi a feugiat dolor, in tristique elit. Mauris feugiat aliquam vulputate. Etiam sed mi quis velit commodo mollis et eu quam. Vestibulum mollis at dolor sed egestas.</p>
    </div>
    <h3>Special Offers</h3>
    <ul class="ticks">
      <li><svg width="11" height="11"><circle cx="5.5" cy="5.5" r="5.5" fill="#9bcb3c"/><path d="M3 5.6l1.8 1.8L8 4" stroke="#fff" stroke-width="1.4" fill="none"/></svg>Lorem ipsum dolor sit amet, consectetur adipiscing elit.</li>
      <li><svg width="11" height="11"><circle cx="5.5" cy="5.5" r="5.5" fill="#9bcb3c"/><path d="M3 5.6l1.8 1.8L8 4" stroke="#fff" stroke-width="1.4" fill="none"/></svg>Sed quis nisi euismod, fermentum tellus a, lobortis quam.</li>
      <li><svg width="11" height="11"><circle cx="5.5" cy="5.5" r="5.5" fill="#9bcb3c"/><path d="M3 5.6l1.8 1.8L8 4" stroke="#fff" stroke-width="1.4" fill="none"/></svg>Vestibulum condimentum mi vitae diam tristique</li>
    </ul>
  </div>
</section>

<footer class="site-footer">
  <div class="wrap">
    <div class="foot-nav"><span>Home</span><span>About us</span><span>Cosmetic Injections</span><span>Podiatry</span><span>Remedial Massage</span><span>Laser Therapies</span><span>Skin Care</span><span>Customer Club &amp; Special Offers</span></div>
    <div class="foot-row">
      <span class="copyright">© Copyright Fernhollow Podiatry 2014</span>
      <div class="contact">
        <span><i class="ico"></i>(03) 9412 0738</span>
        <span><i class="ico"></i>info@fernhollowfootcare.com.au</span>
      </div>
      <div class="social"><i></i><i></i><i></i><i></i></div>
    </div>
  </div>
</footer>

</body>
</html>
```